out of the box Business Card Design for a Manufacturer / Distributor

We are a manufarturer and distributor of products.
the company name is VORTANI (Pic attached)

the picture is NOT a must have on the business Card.

the Business Card should look really professional and/or special, so out of the box thinking is welcome.

there should be 2 Adresses on the Business Card for Main and Branch Office.
Email Adress, homepage, Name is required
NO Phone Number

Our working field:
Private Labeling
high Quality Production
direct distribution
warehousing
trademark registration
legal support

Main Office:
Kornblumenweg 14
08352 Burgstädt
Germany

Branch Office:
Daska Lane
Sialkot
Pakistan

Names:
Lukas Feldhaus (Owner)
Imran Qureshi (Owner)

Email:
lukas@vortani-example.com
imran@vortani-example.com

homepage:
vortani-example.com

Industry/Entity Type

Manufacturer Distributer

Contact Information for Business Card

Vortani

Requirements
Must have
• Names, both office Adresses, email, homepage
Should not have
• Phone Number

```html
<!DOCTYPE html>
<html lang="en">
<head>
<meta charset="utf-8">
<title>Vortani Business Card</title>
<link href="https://fonts.googleapis.com/css2?family=Nunito+Sans:wght@400&family=Poppins:wght@400;700&display=swap" rel="stylesheet">
<style>
  :root {
    --bg: #e5e4e2;
    --lime: #aecc0a;
    --ink: #2b2b2b;
    --paper: #ffffff;
  }
  * { margin: 0; padding: 0; box-sizing: border-box; }
  html, body {
    width: 1197px; height: 1200px; overflow: hidden;
    background: var(--bg);
    font-family: "Poppins", sans-serif;
  }
  .canvas { position: relative; width: 1197px; height: 1200px; }

  .card { position: absolute; top: 445px; width: 542px; height: 309px; overflow: hidden; }
  .card-front { left: 51px; background: var(--paper); }
  .card-back { left: 604px; background: var(--lime); }

  .wordmark {
    position: absolute; display: flex; align-items: center; gap: 14px;
    font-family: "Nunito Sans", sans-serif; font-weight: 400;
    letter-spacing: 1px; line-height: 1; white-space: nowrap;
  }
  .wordmark .dot { width: 40px; height: 40px; border-radius: 50%; flex: none; }
  .card-front .wordmark { left: 150px; top: 80px; font-size: 46px; color: var(--ink); }
  .card-front .wordmark .dot { background: var(--lime); }
  .card-back .wordmark { left: 140px; top: 130px; font-size: 50px; color: var(--paper); }
  .card-back .wordmark .dot { background: var(--paper); }

  .accent-block { position: absolute; left: 0; top: 204px; width: 45px; height: 61px; background: var(--lime); }

  .person { position: absolute; left: 62px; top: 212px; color: var(--ink); white-space: nowrap; }
  .person-name { font-weight: 700; font-size: 19px; line-height: 1.1; }
  .person-role { font-weight: 400; font-size: 12px; line-height: 1.1; }

  .office-band {
    position: absolute; left: 230px; top: 204px; width: 312px; height: 61px;
    background: var(--lime); color: var(--paper);
  }
  .office { position: absolute; top: 13px; font-size: 10px; line-height: 1.3; white-space: nowrap; }
  .office-branch { left: 29px; }
  .office-main { left: 165px; }
  .office-label { font-weight: 700; }

  .contact-row {
    position: absolute; right: 14px; top: 273px; display: flex; align-items: center;
    font-size: 9.5px; line-height: 1; color: var(--ink); white-space: nowrap;
  }
  .contact-item { display: flex; align-items: center; gap: 6px; }
  .contact-item + .contact-item { margin-left: 8px; }
  .contact-item svg { flex: none; }
</style>
</head>
<body>
<div class="canvas">

  <section class="card card-front">
    <div class="wordmark"><span class="dot"></span><span>VORTANI</span></div>

    <div class="accent-block"></div>
    <div class="person">
      <div class="person-name">Imran Qureshi</div>
      <div class="person-role">Owner</div>
    </div>

    <div class="office-band">
      <div class="office office-branch">
        <div class="office-label">Branch Office:</div>
        <div>Daska Lane</div>
        <div>Sialkot Pakistan</div>
      </div>
      <div class="office office-main">
        <div class="office-label">Main Office:</div>
        <div>Kornblumenweg 14 08352</div>
        <div>Burgstadt Germany</div>
      </div>
    </div>

    <div class="contact-row">
      <div class="contact-item">
        <svg width="11" height="8" viewBox="0 0 11 8"><rect width="11" height="8" fill="#aecc0a"/><path d="M0 0 L5.5 4.5 L11 0" fill="none" stroke="#fff" stroke-width="1"/></svg>
        <span>imran@vortani-example.com</span>
      </div>
      <div class="contact-item">
        <svg width="10" height="10" viewBox="0 0 10 10"><circle cx="5" cy="5" r="5" fill="#aecc0a"/><path d="M0 5 H10 M5 0 V10 M5 0 C2 3 2 7 5 10 M5 0 C8 3 8 7 5 10" fill="none" stroke="#fff" stroke-width="0.6"/></svg>
        <span>www.vortani-example.com</span>
      </div>
    </div>
  </section>

  <section class="card card-back">
    <div class="wordmark"><span class="dot"></span><span>VORTANI</span></div>
  </section>

</div>
</body>
</html>
```